Zielgruppe
Hypnose
Aufgabenstellung
Text Vorder- und Rückseite siehe Anlage
Auf der Vorderseite Foto und Logo (auch in der Anlage)
Farbgestaltung passend zu den Logofarben
Das Design soll kreativ und freundlich sein

```html
<!DOCTYPE html>
<html lang="de">
<head>
<meta charset="utf-8">
<title>ruhepol – Flyer</title>
<link href="https://fonts.googleapis.com/css2?family=Quicksand:wght@500;700&family=Dancing+Script:wght@500&display=swap" rel="stylesheet">
<style>
  :root {
    --coral: #e8532a;
    --teal: #2a9db5;
    --rose: #e06a8a;
    --sun: #f2c94c;
    --ink: #5a5a5a;
    --paper: #ffffff;
    --bg: #ffffff;
  }
  * { box-sizing: border-box; margin: 0; padding: 0; }
  html, body { width: 1022px; height: 1200px; overflow: hidden; background: var(--bg); }
  body { position: relative; font-family: "Quicksand", sans-serif; font-weight: 500; }

  .page { position: absolute; background: var(--paper); overflow: hidden; }
  .page--front { left: 63px; top: 134px; width: 426px; height: 882px; }
  .page--back { left: 518px; top: 215px; width: 422px; height: 874px; }

  /* Front */
  .portrait-area {
    position: absolute; left: 0; top: 290px; width: 100%; height: 592px;
    background:
      radial-gradient(ellipse 55% 45% at 58% 62%, rgba(247,196,186,0.95), rgba(247,196,186,0) 70%),
      linear-gradient(180deg, #ffffff 0%, #e9e6e2 22%, #b9ada0 45%, #a89a8c 62%, #d9cfc8 85%, #f4eeee 100%);
  }
  .portrait-fade {
    position: absolute; left: 0; bottom: 0; width: 62%; height: 200px;
    background: linear-gradient(90deg, rgba(255,255,255,0.85), rgba(255,255,255,0));
  }
  .brand {
    position: absolute; right: 30px; top: 92px;
    display: flex; align-items: center; gap: 10px;
  }
  .brand__dot { width: 22px; height: 22px; border-radius: 50%; background: var(--sun); }
  .brand__name { font-size: 24px; font-weight: 700; color: var(--coral); line-height: 1; }

  .motto {
    font-family: "Dancing Script", cursive; color: var(--teal);
    line-height: 27px;
  }
  .motto--front { position: absolute; right: 30px; top: 203px; text-align: right; font-size: 25px; }
  .motto--back { position: absolute; left: 0; width: 100%; top: 722px; text-align: center; font-size: 29px; line-height: 32px; }

  .contact { position: absolute; left: 38px; top: 690px; color: var(--coral); font-size: 13px; line-height: 17px; }
  .contact strong { font-weight: 700; }
  .contact p + p { margin-top: 17px; }

  /* Back */
  .wash {
    position: absolute; inset: 0;
    background:
      radial-gradient(ellipse 80% 30% at 50% 10%, rgba(246,228,170,0.55), rgba(246,228,170,0) 75%),
      radial-gradient(ellipse 90% 35% at 45% 88%, rgba(236,180,206,0.6), rgba(236,180,206,0) 75%);
  }
  .content { position: absolute; left: 63px; width: 297px; }
  .heading { font-size: 18px; font-weight: 700; letter-spacing: .3px; }
  .heading--rose { color: var(--rose); position: absolute; left: 63px; top: 42px; white-space: nowrap; }
  .heading--teal { color: var(--teal); position: absolute; left: 63px; top: 505px; }
  .copy { color: var(--ink); font-size: 13px; line-height: 22.5px; text-align: justify; letter-spacing: .2px; }
  .copy--intro { top: 78px; }
  .copy--about { top: 543px; letter-spacing: 0; }

  .topics { position: absolute; left: 30px; top: 207px; list-style: none; }
  .topics li { display: flex; align-items: center; height: 20.2px; font-size: 13px; letter-spacing: .2px; }
  .topics li::before {
    content: ""; width: 9px; height: 9px; border-radius: 50% 0 50% 0; margin: 0 24px 0 5px;
    transform: rotate(-45deg);
  }
  .topics li:nth-child(odd) { color: var(--coral); }
  .topics li:nth-child(odd)::before { background: var(--sun); opacity: .7; }
  .topics li:nth-child(even) { color: var(--teal); }
  .topics li:nth-child(even)::before { background: #8cc9d8; }
</style>
</head>
<body>

<section class="page page--front">
  <div class="portrait-area" role="img" aria-label="Porträtfoto der Hypnosetrainerin in rosa Jacke vor einem herbstlichen Weingarten"></div>
  <div class="portrait-fade"></div>

  <div class="brand">
    <span class="brand__dot"></span>
    <span class="brand__name">ruhepol</span>
  </div>

  <p class="motto motto--front">Sie brauchen nicht daran zu glauben,<br>Sie brauchen es nur zuzulasen.<br>Sie werden begeistert sein!</p>

  <div class="contact">
    <p>Mag. <strong>Lena Kelbrinos</strong>, BEd MSc<br>Diplomierte Hypnosetrainerin</p>
    <p><strong>Kontakt:</strong> 0670/5518203<br>info@ruhepol-hypnose.at</p>
    <p>Am Lindenhang 14<br>2351 Wiesenau<br>https://ruhepol-hypnose.at</p>
  </div>
</section>

<section class="page page--back">
  <div class="wash"></div>

  <h2 class="heading heading--rose">Wie Hypnose Ihr Leben verändert</h2>
  <p class="content copy copy--intro">Hypnose ist eine wunderbare Möglichkeit, das eigene Leben zu verbessern. Die Anwendungsbereiche sind unglaublich vielfältig – wenn einer der folgenden Punkte auf Sie zutrifft, sind Sie bei mir richtig:</p>

  <ul class="topics">
    <li>Wunsch mit dem Rauchen aufzuhören</li>
    <li>Wunsch abzunehmen</li>
    <li>Prüfungsangst/Lernblockaden</li>
    <li>Höhenangst</li>
    <li>Platzangst</li>
    <li>Flugangst</li>
    <li>Unsicherheit in Menschenmengen</li>
    <li>Wohlbefinden steigern und Entspannung finden</li>
    <li>Schlafstörungen</li>
    <li>Frust</li>
    <li>Trauer</li>
    <li>Erschöpfung/Überforderung</li>
    <li>Lampenfieber</li>
    <li>Selbstvertrauen steigern</li>
  </ul>

  <h2 class="heading heading--teal">Was ist Hypnose?</h2>
  <p class="content copy copy--about">Hypnose ist ein Zustand tiefer Entspannung der genutzt werden kann, um erwünschte Gewohnheiten und Handlungsmuster zu verstärken oder unerwünschte aufzulösen. Zusätzlich ist Hypnose hervorragend geeignet, bei Stress oder Überforderung für innere Ruhe und Wohlbefinden zu sorgen.</p>

  <p class="motto motto--back">Sie brauchen nicht daran zu glauben,<br>Sie brauchen es nur zuzulasen.<br>Sie werden begeistert sein!</p>
</section>

</body>
</html>
```